HARD MONEY ORIGINATOR RECRUITMENT.
Looking for individuals to help us originate loans for real estate investor financing primarily used to fix up properties and resell.
HARD MONEY ORIGINATORS WANTED
No Licensing Required
Work As Independent Contractor
1% Flat Finders Fee on Each Loan
Referral Compensation for Recruiting New Originators
Immediate Payouts
Programs Offered Nationwide
Marketing Assistance and Support Available
Email mpelton@brightquaylending.com for more information or call (800) 641-2950 Ext. 24 Brightquay Lending Services, Inc. www.brightquaylending.com NMLS #318760
Industry/Entity Type
Real Estate
Look and feel
Each slider illustrates characteristics of the customer's brand and the style your logo design should communicate.

```html
<!DOCTYPE html>
<html lang="en">
<head>
<meta charset="utf-8">
<title>Hard Money Originators Wanted</title>
<link href="https://fonts.googleapis.com/css2?family=Anton&family=Archivo+Narrow:wght@600;700&display=swap" rel="stylesheet">
<style>
  :root {
    --brown-dark: #3b2a1f;
    --brown: #4a3426;
    --brown-mid: #6b4c36;
    --paper: #ffffff;
    --panel-grey: #ecebe9;
    --ink: #1f1f1f;
    --gold: #b89a4e;
    --navy: #3a5a9c;
  }
  * { margin: 0; padding: 0; box-sizing: border-box; }
  html, body { width: 797px; height: 1200px; overflow: hidden; background: #d9d6d2; }
  .flyer {
    position: relative;
    width: 797px; height: 1200px;
    background: var(--paper);
    overflow: hidden;
    font-family: "Archivo Narrow", "Arial Narrow", sans-serif;
  }
  .header {
    position: absolute; left: 0; top: 0; width: 797px; height: 185px;
    display: flex; align-items: center; justify-content: center;
  }
  .brand { display: flex; align-items: center; gap: 14px; }
  .brand-dot { width: 30px; height: 30px; border-radius: 50%; background: var(--gold); }
  .brand-name {
    font-family: "Archivo Narrow", sans-serif; font-weight: 700;
    font-size: 30px; color: var(--navy); letter-spacing: 0.5px;
  }
  .band { position: absolute; left: 0; top: 170px; }
  .hero-photo {
    position: absolute; left: 290px; top: 215px; width: 507px; height: 420px;
    background: linear-gradient(160deg, #e9e4dc 0%, #c9b9a4 45%, #7a6a5c 100%);
  }
  .title-panel {
    position: absolute; left: 0; top: 215px; width: 330px; height: 460px;
    background: linear-gradient(180deg, var(--brown) 0%, var(--brown-dark) 100%);
    padding: 40px 0 0 34px;
  }
  .title {
    font-family: "Anton", "Impact", sans-serif; color: var(--paper);
    text-transform: uppercase; line-height: 1.02; font-weight: 400;
  }
  .title .l1 { display: block; font-size: 82px; }
  .title .l2 { display: block; font-size: 82px; }
  .title .l3 { display: block; font-size: 50px; }
  .title .l4 { display: block; font-size: 50px; }
  .gallery {
    position: absolute; left: 0; top: 600px; width: 797px; height: 260px;
  }
  .gallery-strip {
    position: absolute; left: 0; top: 75px; width: 797px; height: 170px; background: var(--panel-grey);
  }
  .thumb {
    position: absolute; border: 8px solid var(--brown-dark); background-clip: padding-box;
    box-shadow: 0 0 0 3px #ffffff inset;
  }
  .thumb-interior { left: 24px; top: 70px; width: 230px; height: 200px;
    background: linear-gradient(160deg, #d8a86a, #8a5a2c); }
  .thumb-desk { left: 300px; top: 20px; width: 190px; height: 190px;
    background: linear-gradient(160deg, #efe9e0, #9aa4b4); }
  .thumb-site { left: 530px; top: 0px; width: 210px; height: 190px;
    background: linear-gradient(160deg, #f0e6cf, #b7a182); }
  .perks {
    position: absolute; left: 60px; top: 885px; list-style: none;
  }
  .perks li {
    display: flex; align-items: center; gap: 14px;
    font-weight: 700; font-size: 29px; color: var(--ink); line-height: 31px;
  }
  .perks svg { flex: none; }
  .contact {
    position: absolute; left: 0; top: 1110px; width: 797px; height: 90px;
    background: var(--brown-dark); color: var(--paper);
    display: flex; flex-direction: column; align-items: center; justify-content: center;
    font-weight: 700; font-style: normal; font-size: 20px; line-height: 28px; text-align: center;
  }
</style>
</head>
<body>
<main class="flyer">
  <header class="header">
    <div class="brand">
      <span class="brand-dot"></span>
      <span class="brand-name">Brightquay Lending Services, Inc.</span>
    </div>
  </header>

  <svg class="band" width="797" height="45" viewBox="0 0 797 45" aria-hidden="true">
    <polygon points="0,15 797,0 797,30 0,45" fill="var(--brown-dark)"/>
  </svg>

  <div class="hero-photo" role="img" aria-label="Smiling builder in a yellow hard hat carrying lumber on his shoulder"></div>

  <section class="title-panel">
    <h1 class="title">
      <span class="l1">Hard</span>
      <span class="l2">Money</span>
      <span class="l3">Originators</span>
      <span class="l4">Wanted</span>
    </h1>
  </section>

  <section class="gallery">
    <div class="gallery-strip"></div>
    <div class="thumb thumb-interior" role="img" aria-label="Wooden house interior under renovation"></div>
    <div class="thumb thumb-desk" role="img" aria-label="Carpenter smiling at a workbench"></div>
    <div class="thumb thumb-site" role="img" aria-label="Two contractors in hard hats reviewing plans on site"></div>
  </section>

  <ul class="perks">
    <li><svg width="16" height="16" viewBox="0 0 16 16"><path d="M0 0 L9 8 L0 16 Z M7 0 L16 8 L7 16 Z" fill="var(--brown-dark)"/></svg>No Licensing Required</li>
    <li><svg width="16" height="16" viewBox="0 0 16 16"><path d="M0 0 L9 8 L0 16 Z M7 0 L16 8 L7 16 Z" fill="var(--brown-dark)"/></svg>Work As Independent Contractor</li>
    <li><svg width="16" height="16" viewBox="0 0 16 16"><path d="M0 0 L9 8 L0 16 Z M7 0 L16 8 L7 16 Z" fill="var(--brown-dark)"/></svg>1% Flat Finders Fee on Each Loan</li>
    <li><svg width="16" height="16" viewBox="0 0 16 16"><path d="M0 0 L9 8 L0 16 Z M7 0 L16 8 L7 16 Z" fill="var(--brown-dark)"/></svg>Referral Compensation for Recruiting New Originators</li>
    <li><svg width="16" height="16" viewBox="0 0 16 16"><path d="M0 0 L9 8 L0 16 Z M7 0 L16 8 L7 16 Z" fill="var(--brown-dark)"/></svg>Immediate Payouts</li>
    <li><svg width="16" height="16" viewBox="0 0 16 16"><path d="M0 0 L9 8 L0 16 Z M7 0 L16 8 L7 16 Z" fill="var(--brown-dark)"/></svg>Programs Offered Nationwide</li>
    <li><svg width="16" height="16" viewBox="0 0 16 16"><path d="M0 0 L9 8 L0 16 Z M7 0 L16 8 L7 16 Z" fill="var(--brown-dark)"/></svg>Marketing Assistance and Support Available</li>
  </ul>

  <footer class="contact">
    <p>Email mpelton@brightquaylending.com for more information or call (800) 641-2950 Ext. 24</p>
    <p>Brightquay Lending Services, Inc. www.brightquaylending.com NMLS #318760</p>
  </footer>
</main>
</body>
</html>
```